Belford & Company

We are a boutique commercial real estate firm. For our Business card design - sleek, modern, yet high-end/classy. Please see our website: belfordandcompany.example for details.

We currently need 2 business card names and the ability to add/change the business card information -
Name, Title, Address, Office #, Mobile #, Fax, Email and company website.

Industry/Entity Type

Real Estate

Contact Information for Business Card

Business card design - sleek, modern, yet high-end/classy. Please see our website: belfordandcompany.example for details.

Also, we'd like to have our slogan "Diligence Makes The Difference." somewhere in there. We'd like to make some part of it raised or a different texture if possible.
Color #'s:
blue 19 36 128
light gray 222 222 221
dark gray 107 120 128

Also, we'd like to have our slogan "Diligence Makes The Difference." somewhere in there. We'd like to make some part of it raised or a different texture if possible - grey on one side and blue on the other - rounded edges preferred. Maybe either metal/silver/grey raised logo on the back. Thank you!!

Requirements
Must have
• Sleek, modern, clean and classy design

```html
<!DOCTYPE html>
<html lang="en">
<head>
<meta charset="utf-8">
<title>Belford &amp; Company – Business Card</title>
<link href="https://fonts.googleapis.com/css2?family=Mulish:wght@400;600;800&display=swap" rel="stylesheet">
<style>
  :root {
    --brand-blue: #2f4ea6;
    --brand-blue-deep: #1f3590;
    --brand-blue-light: #4566bd;
    --paper: #ffffff;
    --light-gray: #dededd;
    --dark-gray: #6b7880;
    --ink: #2a2f36;
    --backdrop: #e9eaec;
  }
  * { box-sizing: border-box; margin: 0; padding: 0; }
  html, body {
    width: 1200px; height: 900px; overflow: hidden;
    background: var(--backdrop);
    font-family: "Mulish", Arial, sans-serif;
  }
  .sheet {
    width: 1200px; height: 900px;
    display: flex; flex-direction: column; align-items: center; justify-content: center;
    gap: 40px;
  }
  .card {
    width: 700px; height: 400px;
    border-radius: 18px;
    overflow: hidden;
    box-shadow: 0 10px 28px rgba(20, 30, 60, 0.18);
    position: relative;
  }

  /* Company name: one colour, one weight of the text font */
  .company-name {
    display: flex; align-items: center; gap: 10px;
    color: var(--paper); font-weight: 600; white-space: nowrap;
  }
  .company-name-square { background: var(--paper); flex: none; }

  /* Front */
  .card-front { display: flex; background: var(--paper); }
  .front-brand {
    width: 262px; height: 100%;
    background: linear-gradient(160deg, var(--brand-blue-light), var(--brand-blue));
    display: flex; align-items: flex-end; padding: 0 26px 104px;
  }
  .front-brand .company-name { font-size: 20px; }
  .front-brand .company-name-square { width: 10px; height: 10px; }
  .front-details { flex: 1; position: relative; padding: 0 34px; }
  .rule-top {
    position: absolute; left: 0; right: 0; top: 64px;
    height: 3px; background: var(--brand-blue-deep);
  }
  .person { position: absolute; left: 34px; top: 80px; }
  .person-name { color: var(--brand-blue); font-weight: 800; font-size: 30px; }
  .person-title { color: var(--ink); font-size: 17px; margin-top: 2px; font-weight: 400; }
  .rule-mid {
    position: absolute; left: 0; right: 0; top: 158px;
    height: 2px; background: var(--light-gray);
  }
  .contact-list {
    position: absolute; left: 34px; top: 182px;
    list-style: none; color: var(--ink); font-size: 16px; line-height: 1.3;
  }
  .contact-list li { display: flex; align-items: flex-start; gap: 16px; margin-bottom: 16px; }
  .contact-list svg { width: 22px; height: 22px; flex: none; margin-top: 1px; }

  /* Back */
  .card-back {
    background: linear-gradient(150deg, var(--brand-blue-light) 0%, var(--brand-blue) 55%, var(--brand-blue-deep) 100%);
    display: flex; align-items: center; justify-content: center;
  }
  .card-back .company-name { font-size: 34px; gap: 14px; }
  .card-back .company-name-square { width: 16px; height: 16px; }
  .back-website {
    position: absolute; right: 40px; bottom: 30px;
    color: var(--paper); font-size: 18px; font-weight: 600;
  }
</style>
</head>
<body>
<main class="sheet">
  <section class="card card-front" aria-label="Business card front">
    <div class="front-brand">
      <p class="company-name"><span class="company-name-square"></span><span>Belford &amp; Company</span></p>
    </div>
    <div class="front-details">
      <div class="rule-top"></div>
      <div class="person">
        <h1 class="person-name">Daniel Hartley</h1>
        <p class="person-title">President</p>
      </div>
      <div class="rule-mid"></div>
      <ul class="contact-list">
        <li>
          <svg viewBox="0 0 24 24" aria-hidden="true"><path d="M12 3 2 12h3v9h5v-6h4v6h5v-9h3z" fill="#222"/></svg>
          <span>2310 Harbor View Rd., Suite #118<br>Marlow Bay, FL 30418</span>
        </li>
        <li>
          <svg viewBox="0 0 24 24" aria-hidden="true"><path d="M6.5 3.5 9 6.5 7.5 9c1.2 2.8 3.5 5.1 6.5 6.5l2.5-1.5 3 2.5-1.5 3C11 19.5 4.5 13 3.5 5z" fill="none" stroke="#222" stroke-width="1.6" stroke-linejoin="round"/></svg>
          <span>555 0142 718</span>
        </li>
        <li>
          <svg viewBox="0 0 24 24" aria-hidden="true"><rect x="3" y="6" width="18" height="12" fill="none" stroke="#222" stroke-width="1.6"/><path d="m3 6 9 7 9-7" fill="none" stroke="#222" stroke-width="1.6"/></svg>
          <span>info@belfordandcompany.example</span>
        </li>
      </ul>
    </div>
  </section>

  <section class="card card-back" aria-label="Business card back">
    <p class="company-name"><span class="company-name-square"></span><span>Belford &amp; Company</span></p>
    <p class="back-website">website: belfordandcompany.example</p>
  </section>
</main>
</body>
</html>
```